Business Card for Quillmark Ledger - A cannabis publication for executives.

I'd like some business cards for Quillmark Ledger. The logo is done (great job!) and I need a card design I will use with PRINTLY. I made it a short project to allow time for printing before an event. These will be standard sized cards (final artwork size 3.66" x 2.16" at 300dpi) with a final card size of 3.5" x 2.0". (See PRINTLY.com if you need more info.) I might try rounded corners but am not sure yet. I think the design will work okay with rounded.

Quillmark Ledger will be a bi-weekly publication for the cannabis industry. It is targeted to investors and industry executives, not consumers or pot smokers. So our market is more B2B. However I am open to creativity and making the card something people remark on.

My contact for card:

Dana Merrow
Founder/CEO
dana@quillmarkledger.example

2740 Harlow Avenue
Boston MA 02135
(617)555-0194

Target Market(s)

Executives, Industry people and investors in the Cannabis sector.

Contact Information for Business Card

PRINTLY does do double sided and the second side can be the same or different images. Only one side is required but use of the second side would be a bonus.

Font styles to use
Serif
Sans Serif
Decorative

Colors

Designer to choose colors to be used in the design.

Requirements
Must have
• Logo, contact info
Nice to have
• Style and design to make the card stand out in a crowd.

```html
<!DOCTYPE html>
<html lang="en">
<head>
<meta charset="utf-8">
<title>Quillmark Ledger — Business Card</title>
<link rel="stylesheet" href="https://fonts.googleapis.com/css2?family=Open+Sans:wght@400;600&family=Oswald:wght@500&display=swap">
<style>
  :root {
    --backdrop: #cdcdd0;
    --card: #ffffff;
    --brand-blue: #1a78c2;
    --brand-green: #6cb33f;
    --ink: #3a3a3a;
    --rule: #444444;
  }
  * { box-sizing: border-box; margin: 0; padding: 0; }
  html, body { width: 1200px; height: 1200px; overflow: hidden; }
  body {
    background: var(--backdrop);
    font-family: "Open Sans", Arial, sans-serif;
    display: flex;
    flex-direction: column;
    align-items: center;
    justify-content: center;
    gap: 60px;
  }
  .card {
    position: relative;
    width: 900px;
    height: 514px;
    background: var(--card);
    border-radius: 30px;
    box-shadow: 0 6px 14px rgba(0,0,0,0.18);
  }
  /* Front */
  .card--front { display: flex; align-items: center; justify-content: center; }
  .brand { display: flex; align-items: center; gap: 22px; }
  .brand__dot {
    width: 64px; height: 64px; border-radius: 50%;
    background: var(--brand-green);
  }
  .brand__name {
    font-weight: 600; font-size: 62px; color: var(--brand-blue);
    letter-spacing: -0.5px;
  }
  /* Back */
  .identity {
    position: absolute; top: 170px; left: 0; right: 0;
    display: flex; justify-content: center; align-items: center; gap: 28px;
  }
  .person { text-align: right; }
  .person__name {
    font-family: "Oswald", "Arial Narrow", sans-serif;
    font-weight: 500; font-size: 40px; line-height: 1; letter-spacing: -0.5px;
  }
  .person__first { color: var(--brand-blue); }
  .person__last { color: var(--brand-green); }
  .person__title { font-size: 19px; color: var(--ink); margin-top: 6px; }
  .divider { width: 2px; height: 100px; background: var(--rule); }
  .contacts { list-style: none; font-size: 19px; color: var(--ink); line-height: 1.5; }
  .contacts li { display: flex; align-items: center; gap: 10px; }
  .contacts svg { width: 17px; height: 17px; fill: var(--brand-blue); flex: none; }
  .address {
    position: absolute; bottom: 70px; left: 0; right: 0;
    text-align: center; font-size: 22px; color: var(--ink);
  }
  .address__brand-a { color: var(--brand-blue); }
  .address__brand-b { color: var(--brand-green); }
</style>
</head>
<body>
  <section class="card card--front" aria-label="Card front">
    <div class="brand">
      <span class="brand__dot"></span>
      <span class="brand__name">Quillmark Ledger</span>
    </div>
  </section>

  <section class="card card--back" aria-label="Card back">
    <div class="identity">
      <div class="person">
        <div class="person__name"><span class="person__first">DANA</span> <span class="person__last">MERROW</span></div>
        <div class="person__title">Founder/CEO</div>
      </div>
      <div class="divider"></div>
      <ul class="contacts">
        <li><svg viewBox="0 0 24 24" aria-hidden="true"><path d="M6.6 10.8a15.1 15.1 0 0 0 6.6 6.6l2.2-2.2c.3-.3.7-.4 1-.2 1.1.4 2.3.6 3.6.6.6 0 1 .4 1 1V20c0 .6-.4 1-1 1A17 17 0 0 1 3 4c0-.6.4-1 1-1h3.5c.6 0 1 .4 1 1 0 1.3.2 2.5.6 3.6.1.3 0 .7-.2 1z"/></svg>(617)555-0194</li>
        <li><svg viewBox="0 0 24 24" aria-hidden="true"><path d="M2 5h20v14H2z M2 5l10 8 10-8" stroke="#fff" stroke-width="1.6"/></svg>dana@quillmarkledger.example</li>
        <li><svg viewBox="0 0 24 24" aria-hidden="true"><circle cx="12" cy="12" r="10"/><path d="M2 12h20M12 2c3 3 3 17 0 20M12 2c-3 3-3 17 0 20" stroke="#fff" stroke-width="1.4" fill="none"/></svg>www.quillmarkledger.example</li>
      </ul>
    </div>
    <p class="address"><span class="address__brand-a">Quillmark</span> <span class="address__brand-b">Ledger:</span> 2740 Harlow Avenue Boston MA 02135</p>
  </section>
</body>
</html>
```